3 App Screens Designed

I have a laundry app and the developers want 3 images to replace the standard 3 attached.

The images should be custom made with a laundry theme and NOT downloaded from an image site

The app background will be white and the images I need to submit must be 1024 x 1024 with transparent background.

NOTE: I only need the images and not the app face.

Thanks

Colors
0054AA
0677BA
7BADD7
CADEEF
E8F1F8

```html
<!DOCTYPE html>
<html lang="en">
<head>
<meta charset="UTF-8">
<title>Receive Your Clean Items</title>
<link href="https://fonts.googleapis.com/css2?family=Open+Sans:wght@400;700&display=swap" rel="stylesheet">
<style>
  :root {
    --brand-deep: #0054AA;
    --brand-mid: #0677BA;
    --brand-soft: #7BADD7;
    --brand-pale: #CADEEF;
    --brand-mist: #E8F1F8;
    --paper: #FFFFFF;
    --ink: #253F9A;
  }
  * { margin: 0; padding: 0; box-sizing: border-box; }
  html, body {
    width: 867px;
    height: 1200px;
    overflow: hidden;
    background: var(--paper);
  }
  .onboarding-screen {
    position: relative;
    width: 867px;
    height: 1200px;
    background: var(--paper);
    font-family: "Open Sans", Arial, sans-serif;
  }
  .delivery-van {
    position: absolute;
    left: 243px;
    top: 240px;
    width: 381px;
    height: 212px;
  }
  .delivery-van .outline {
    fill: none;
    stroke: var(--ink);
    stroke-width: 4;
    stroke-linejoin: round;
    stroke-linecap: round;
  }
  .delivery-van .wheel {
    fill: var(--paper);
    stroke: var(--ink);
    stroke-width: 4;
  }
  .screen-title {
    position: absolute;
    left: 0;
    top: 690px;
    width: 867px;
    font-size: 28px;
    font-weight: 700;
    color: var(--ink);
    text-align: center;
  }
  .screen-description {
    position: absolute;
    left: 213px;
    top: 780px;
    width: 441px;
    font-size: 15px;
    line-height: 32px;
    color: var(--ink);
    text-align: center;
  }
</style>
</head>
<body>
  <main class="onboarding-screen">
    <svg class="delivery-van" viewBox="0 0 180 100" role="img" aria-label="Delivery van bringing clean laundry">
      <path class="outline" d="M8 14 Q8 6 16 6 H120 Q126 6 130 11 L152 38 Q155 42 161 43 L166 44 Q172 46 172 53 V74 Q172 80 166 80 H14 Q8 80 8 74 Z"/>
      <path class="outline" d="M118 18 H128 Q131 18 133 21 L146 38 H118 Z"/>
      <line class="outline" x1="162" y1="56" x2="168" y2="56"/>
      <circle class="wheel" cx="50" cy="80" r="12"/>
      <circle class="wheel" cx="140" cy="80" r="12"/>
      <circle class="wheel" cx="50" cy="80" r="4"/>
      <circle class="wheel" cx="140" cy="80" r="4"/>
    </svg>
    <h1 class="screen-title">Receive Your Clean Items</h1>
    <p class="screen-description">You'll be notified that your clothes are ready. Set up a delivery and clean, fresh clothes will be on their way to your door.</p>
  </main>
</body>
</html>
```